Packaging artwork design for furniture

Currently our packaging is utilitarian. We want a new look that reflects our new exciting branding strategy. We want the packaging to reflect a sophisticated, expensive look. I have attached the current packaging and the logo. All the information on the box are required for the new design.
Please use between 2-3 colours, not more.

Target Market(s)

International

Industry/Entity Type

furniture

Requirements
Must have
• All the symbols but need some extra artwork
Nice to have
• artwork that portrays high end, expensive look

```html
<!DOCTYPE html>
<html lang="en">
<head>
<meta charset="utf-8">
<title>Larkfield Living — Night Table Carton</title>
<link rel="stylesheet" href="https://fonts.googleapis.com/css2?family=Lora:wght@500&family=Roboto+Condensed:wght@400&display=swap">
<style>
  :root {
    --stage: #dcdcdc;
    --slate: #3c4447;
    --slate-light: #5f6769;
    --tan: #e6b97d;
    --tan-side: #cf9f62;
    --tan-deep: #d9a867;
    --ink: #3f4649;
  }
  * { margin: 0; padding: 0; box-sizing: border-box; }
  html, body { width: 1200px; height: 1200px; overflow: hidden; }
  body {
    background: var(--stage);
    position: relative;
    font-family: "Roboto Condensed", Arial, sans-serif;
  }
  .carton {
    position: absolute;
    top: 180px;
    left: 110px;
    display: flex;
    height: 840px;
  }
  .panel {
    position: relative;
    height: 100%;
    overflow: hidden;
  }
  .panel--side { width: 360px; }
  .panel--front { width: 620px; }
  .band-top {
    position: absolute;
    top: 0; left: 0; right: 0;
    height: 400px;
  }
  .panel--side .band-top { background: var(--slate); }
  .panel--front .band-top { background: linear-gradient(180deg, var(--slate-light), var(--slate)); }
  .band-bottom {
    position: absolute;
    top: 400px; left: 0; right: 0; bottom: 0;
  }
  .panel--side .band-bottom { background: linear-gradient(180deg, var(--tan-side), var(--tan-deep)); }
  .panel--front .band-bottom { background: linear-gradient(180deg, var(--tan), var(--tan-deep)); }

  .handling-symbols {
    position: absolute;
    top: 100px;
    left: 50px;
    display: flex;
    gap: 6px;
  }
  .handling-symbols svg { width: 44px; height: 58px; }

  .brand {
    position: absolute;
    left: 0; right: 0;
    display: flex;
    align-items: center;
    justify-content: center;
  }
  .brand-mark {
    display: block;
    background: var(--ink);
    flex: none;
  }
  .brand-name {
    font-family: "Lora", Georgia, serif;
    font-weight: 500;
    color: var(--ink);
    white-space: nowrap;
  }
  .panel--side .brand { top: 420px; gap: 10px; }
  .panel--side .brand-mark { width: 16px; height: 16px; }
  .panel--side .brand-name { font-size: 26px; }
  .panel--front .brand { top: 418px; gap: 16px; }
  .panel--front .brand-mark { width: 30px; height: 30px; }
  .panel--front .brand-name { font-size: 48px; }

  .product-info {
    position: absolute;
    top: 600px;
    left: 70px;
    font-size: 20px;
    line-height: 1.35;
    color: var(--ink);
    list-style: none;
  }
  .orientation-mark {
    position: absolute;
    top: 680px;
    left: 270px;
    width: 80px;
    height: 110px;
  }
</style>
</head>
<body>
  <main class="carton">
    <section class="panel panel--side">
      <div class="band-top"></div>
      <div class="band-bottom"></div>

      <div class="handling-symbols" aria-label="Handling symbols">
        <svg viewBox="0 0 44 58" aria-label="Fragile">
          <rect x="2" y="2" width="40" height="54" fill="none" stroke="var(--tan)" stroke-width="2.5"/>
          <path d="M13 12 h18 l-2 14 a7 7 0 0 1 -14 0 z M22 33 v12 M15 45 h14" fill="none" stroke="var(--tan)" stroke-width="2.5"/>
        </svg>
        <svg viewBox="0 0 44 58" aria-label="This way up">
          <rect x="2" y="2" width="40" height="54" fill="none" stroke="var(--tan)" stroke-width="2.5"/>
          <path d="M15 46 v-30 M9 22 l6-8 6 8 M29 46 v-30 M23 22 l6-8 6 8 M10 49 h24" fill="none" stroke="var(--tan)" stroke-width="2.5"/>
        </svg>
        <svg viewBox="0 0 44 58" aria-label="Keep dry">
          <rect x="2" y="2" width="40" height="54" fill="none" stroke="var(--tan)" stroke-width="2.5"/>
          <path d="M8 28 a14 12 0 0 1 28 0 z" fill="var(--tan)"/>
          <path d="M22 28 v15 a3 3 0 0 1 -6 0" fill="none" stroke="var(--tan)" stroke-width="2.5"/>
        </svg>
        <svg viewBox="0 0 44 58" aria-label="Keep away from sunlight">
          <rect x="2" y="2" width="40" height="54" fill="none" stroke="var(--tan)" stroke-width="2.5"/>
          <circle cx="22" cy="20" r="5" fill="var(--tan)"/>
          <path d="M22 9 v4 M22 27 v4 M11 20 h4 M29 20 h4 M14 12 l3 3 M27 25 l3 3 M30 12 l-3 3 M17 25 l-3 3 M10 48 v-10 l12-7 12 7 v10 z" fill="none" stroke="var(--tan)" stroke-width="2"/>
        </svg>
        <svg viewBox="0 0 44 58" aria-label="Keep away from fire">
          <rect x="2" y="2" width="40" height="54" fill="none" stroke="var(--tan)" stroke-width="2.5"/>
          <path d="M22 12 c8 10 12 16 10 24 a10 10 0 0 1 -20 0 c0 -6 4 -8 6 -14 c2 4 4 5 4 8 c2 -6 1 -12 0 -18 z" fill="var(--tan)"/>
          <path d="M10 48 h24" stroke="var(--tan)" stroke-width="2.5"/>
        </svg>
      </div>

      <div class="brand">
        <span class="brand-mark"></span>
        <p class="brand-name">Larkfield Living</p>
      </div>

      <ul class="product-info">
        <li>Model : KT440-BX07</li>
        <li>Item : NIGHT TABLE</li>
        <li>Quantity : 1/1</li>
        <li>Cbm :</li>
      </ul>
    </section>

    <section class="panel panel--front">
      <div class="band-top"></div>
      <div class="band-bottom"></div>

      <div class="brand">
        <span class="brand-mark"></span>
        <p class="brand-name">Larkfield Living</p>
      </div>

      <svg class="orientation-mark" viewBox="0 0 80 110" aria-label="This way up">
        <path d="M14 90 v-70 M4 32 l10-16 10 16 Z M66 90 v-70 M56 32 l10-16 10 16 Z" fill="var(--ink)" stroke="var(--ink)" stroke-width="5" stroke-linejoin="round"/>
        <text x="40" y="90" text-anchor="middle" font-family="Roboto Condensed, Arial, sans-serif" font-size="20" fill="var(--ink)">UP</text>
        <path d="M8 100 h64" stroke="var(--ink)" stroke-width="5"/>
      </svg>
    </section>
  </main>
</body>
</html>
```